V9 Web Design Project

New company website for Intel cyber security company.

Style should be cool, but remain appropriate for very serious subject matter and audience.

Target Market(s)

Target audience is government and the military

Navigation needs to include:
- About Us
- Services
- Careers
- Contact Us
- Contracts

As well as 2 feature areas - use "Technology Integration" and "Case Study" as the supporting headlines.

Industry/Entity Type

Security

Font styles to use
Sans Serif

Colors

Designer to choose colors to be used in the design.

Requirements
Must have
• Mountain imagery and theme.

Use logo attached.

New Tagline - "Securing the Continuum"
Nice to have
• Supporting imagery could include photos representative of security - avoid cliches.
Should not have
• Needs to be serious not frivolous

```html
<!DOCTYPE html>
<html lang="en">
<head>
<meta charset="utf-8">
<title>V9 GROUP – Securing the Continuum</title>
<link href="https://fonts.googleapis.com/css2?family=Cabin:wght@400;500;600&family=Arimo:wght@400;700&display=swap" rel="stylesheet">
<style>
:root{
  --navy:#1b2b7a;
  --footer:#172673;
  --band:#e1e1e1;
  --text:#555a60;
  --dark:#222;
  --rule:#c9c9c9;
  --link:#1a9fe0;
  --white:#fff;
}
*{box-sizing:border-box;margin:0;padding:0}
h1,h2,h3{font-weight:400}
html,body{width:946px;height:1200px;overflow:hidden;background:var(--white)}
body{position:relative;font-family:"Arimo",Arial,sans-serif;color:var(--text)}
.abs{position:absolute}

/* hero */
.hero{left:0;top:0;width:946px;height:384px;
  background:linear-gradient(160deg,#c9ccd8 0%,#eeeef2 25%,#b9a6b8 55%,#8a5a7c 80%,#6f3f63 100%)}
.header-white{left:144px;top:8px;width:741px;height:82px;background:var(--white)}
.logo-mark{left:62px;top:8px;width:82px;height:82px;background:var(--navy)}
.logo-name{left:162px;top:20px;font-family:"Cabin",sans-serif;font-weight:500;font-size:48px;color:var(--navy);letter-spacing:1px;line-height:56px}
.main-nav{left:452px;top:29px;display:flex;align-items:center;font-family:"Cabin",sans-serif;font-size:13.5px;color:#333}
.main-nav a{color:inherit;text-decoration:none;height:41px;line-height:41px}
.main-nav .active{width:85px;border:1px solid var(--navy);border-radius:2px;text-align:center;color:var(--navy)}
.tagline{left:123px;top:203px;width:331px;height:59px;background:rgba(255,255,255,.6);
  font-family:"Cabin",sans-serif;font-size:28px;color:var(--navy);line-height:59px;text-align:center}
.monitor{left:503px;top:107px;width:341px;height:261px;border-radius:8px;
  background:linear-gradient(135deg,#0c1c8c 0%,#1d54d8 45%,#58b4f4 55%,#1230a8 100%);border:6px solid #111}

/* features */
.section-title{font-family:"Cabin",sans-serif;font-size:20px;color:var(--navy);text-align:center;width:946px;left:0}
.feature-title{font-family:"Cabin",sans-serif;font-size:16.5px;color:var(--navy)}
.feature-text{font-size:10.4px;line-height:18px;letter-spacing:.1px;width:268px}
.btn{display:block;width:108px;height:33px;background:var(--navy);color:var(--white);font-family:"Cabin",sans-serif;font-size:13px;letter-spacing:.4px;text-align:center;line-height:33px;text-decoration:none}

/* welcome */
.welcome{left:0;top:587px;width:946px;height:222px;background:var(--band)}
.welcome-photo{left:61px;top:629px;width:287px;height:164px;background:radial-gradient(circle at 55% 45%,#bfe8ff 0%,#3a8ff0 25%,#10309a 60%,#06124a 100%)}
.welcome-text{left:357px;top:627px;width:510px;font-size:10.7px;line-height:18px;color:#333}
.welcome-text p+p{margin-top:18px}

/* news & tweets */
.col-title{font-family:"Cabin",sans-serif;font-size:20px;color:var(--navy)}
.news{left:70px;top:852px;width:396px}
.news-item{border-bottom:1px solid var(--rule);padding:3px 2px 5px}
.news-date{font-size:9.8px;color:#777;line-height:15px}
.news-body{font-size:10.6px;color:#222;line-height:18px;margin-top:2px}
.tweets-label{left:484px;top:858px;font-size:12.3px;color:#111}
.follow{left:768px;top:855px;width:117px;height:22px;border:1px solid #c8ccd2;border-radius:3px;background:linear-gradient(#fbfbfb,#e8ebef);font-size:10.4px;color:#333;line-height:20px;padding-left:26px}
.follow::before{content:"";position:absolute;left:8px;top:5px;width:11px;height:11px;border-radius:50%;background:var(--link)}
.tweet{left:482px;width:398px;border-bottom:1px solid var(--rule)}
.avatar{position:absolute;left:2px;top:0;width:54px;height:54px;background:linear-gradient(160deg,#d8d0c8,#8c7a6c)}
.tweet-body{margin-left:62px;font-size:9.8px;line-height:18px;color:#222}
.tweet-name{font-weight:700;font-size:11.3px}
.tweet-body .at{color:var(--link)}
.expand{color:#999;font-size:9.5px;line-height:18px}

/* footer */
.footer{left:0;top:1085px;width:946px;height:115px;background:var(--footer);color:var(--white)}
.footer-nav{position:absolute;top:17px;left:0;width:946px;font-family:"Cabin",sans-serif;font-size:13px}
.footer-nav a{position:absolute;color:var(--white);text-decoration:none;transform:translateX(-50%)}
.copyright{position:absolute;left:71px;top:67px;font-size:10px}
.social{position:absolute;top:46px;width:50px;height:51px}
.social span{position:absolute;inset:0;display:flex;align-items:center;justify-content:center;font-family:"Cabin",sans-serif;font-size:10px;color:var(--white)}
</style>
</head>
<body>

<section class="hero abs" role="img" aria-label="Snow-covered mountain range under a pale sky"></section>
<header>
  <div class="header-white abs"></div>
  <div class="logo-mark abs" aria-hidden="true"></div>
  <div class="logo-name abs">V9 GROUP</div>
  <nav class="main-nav abs">
    <a class="active" href="#">About Us</a>
    <a href="#" style="margin-left:21px">Services</a>
    <a href="#" style="margin-left:37px">Careers</a>
    <a href="#" style="margin-left:38px">Contracts</a>
    <a href="#" style="margin-left:36px">Contact</a>
  </nav>
</header>
<h1 class="tagline abs">Securing the Continuum</h1>
<div class="monitor abs" role="img" aria-label="Desktop monitor showing a glowing padlock on a circuit-board security screen"></div>

<!-- features -->
<h2 class="section-title abs" style="top:395px">Features</h2>

<svg class="abs" style="left:71px;top:429px" width="124" height="133" viewBox="0 0 124 133" aria-hidden="true">
  <polygon points="62,1 123,34 123,99 62,132 1,99 1,34" fill="#1b2b7a"/>
  <polygon points="62,7 117,37 117,96 62,126 7,96 7,37" fill="none" stroke="#fff" stroke-width="1"/>
  <circle cx="52" cy="66" r="11" fill="none" stroke="#fff" stroke-width="9" stroke-dasharray="5 3.6"/>
  <circle cx="52" cy="66" r="5" fill="#fff"/>
  <circle cx="76" cy="53" r="6" fill="none" stroke="#fff" stroke-width="6" stroke-dasharray="3 2.6"/>
  <circle cx="78" cy="79" r="6" fill="none" stroke="#fff" stroke-width="6" stroke-dasharray="3 2.6"/>
</svg>
<h3 class="feature-title abs" style="left:208px;top:434px">Technology Integration</h3>
<p class="feature-text abs" style="left:208px;top:463px">Lorem Ipsum is simply dummy text of the printing and typesetting industry. Lorem Ipsum has been the industry's standard dummy text ever since the 1500s</p>
<a class="btn abs" href="#" style="left:207px;top:524px">READ MORE</a>

<svg class="abs" style="left:484px;top:429px" width="124" height="133" viewBox="0 0 124 133" aria-hidden="true">
  <polygon points="62,1 123,34 123,99 62,132 1,99 1,34" fill="#fff" stroke="#1b2b7a" stroke-width="1"/>
  <polygon points="62,5 119,36 119,97 62,128 5,97 5,36" fill="none" stroke="#1b2b7a" stroke-width="1"/>
  <path d="M40 39 H73 L86 52 V94 H40 Z" fill="none" stroke="#111" stroke-width="3.5" stroke-linejoin="round"/>
  <path d="M72 39 V53 H86" fill="none" stroke="#111" stroke-width="3"/>
  <path d="M49 63 H77 M49 71 H77 M49 79 H77 M49 87 H77" stroke="#111" stroke-width="2.5"/>
</svg>
<h3 class="feature-title abs" style="left:621px;top:434px">Case Study</h3>
<p class="feature-text abs" style="left:621px;top:463px">Lorem Ipsum is simply dummy text of the printing and typesetting industry. Lorem Ipsum has been the industry's standard dummy text ever since the 1500s</p>
<a class="btn abs" href="#" style="left:620px;top:524px">READ MORE</a>

<!-- welcome -->
<section class="welcome abs"></section>
<h2 class="section-title abs" style="top:594px">Welcome to V9 GROUP</h2>
<div class="welcome-photo abs" role="img" aria-label="Glowing blue padlock on a circuit board"></div>
<div class="welcome-text abs">
  <p>Lorem Ipsum is simply dummy text of the printing and typesetting industry. Lorem Ipsum has been the industry's standard dummy text ever since the 1500s, when an unknown printer took a galley of type and scrambled it to make a type specimen book. It has survived not only five centuries, but also the leap into lectronic typesetting, remaining essentially unchanged. It was popularised in the 1960s with the rlease of Letraset sheets containing Lorem Ipsum passages, and more recently with desktop publishing software.</p>
  <p>Lorem Ipsum is simply dummy text of the printing and typesetting industry. Lorem Ipsum has been the industry's standard dummy text ever since the 1500s, when an unknown printer took a galley of type lorem Ipsum is simply dummy text of the printing and typesetting industry. Lorem Ipsum has been.</p>
</div>

<!-- news -->
<h2 class="col-title abs" style="left:71px;top:814px">Latest News</h2>
<div class="news abs">
  <div class="news-item"><div class="news-date">Dec 17 2014</div><div class="news-body">Lorem Ipsum is simply dummy text of the printing and typesetting industry. Lorem Ipsum has been the industry's standard dummy text ever since the 1500s.</div></div>
  <div class="news-item"><div class="news-date">Dec 14 2014</div><div class="news-body">Lorem Ipsum is simply dummy text of the printing and typesetting industry. Lorem Ipsum has been the industry's standard dummy text ever since the 1500s.</div></div>
  <div class="news-item"><div class="news-date">Dec 10 2014</div><div class="news-body">Lorem Ipsum is simply dummy text of the printing and typesetting industry.</div></div>
  <div class="news-item"><div class="news-date">Dec 10 2014</div><div class="news-body">Lorem Ipsum is simply dummy text of the printing and typesetting industry.</div></div>
</div>

<!-- tweets -->
<h2 class="col-title abs" style="left:484px;top:814px">Tweets</h2>
<div class="tweets-label abs">Tweets</div>
<div class="follow abs">Follow @v9group</div>
<article class="tweet abs" style="top:883px;height:72px">
  <div class="avatar" role="img" aria-label="Profile photo"></div>
  <div class="tweet-body">
    <div><span class="tweet-name">Halvorn</span> @ Halvorn</div>
    <div>Lorem Ipsum is simply dummy <span class="at">@ dummy text</span> of the printing and typesetting industry. Lorem Ipsum has been the industry's standard dummy text.</div>
    <div class="expand">Expand</div>
  </div>
</article>
<article class="tweet abs" style="top:966px;height:88px">
  <div class="avatar" role="img" aria-label="Profile photo"></div>
  <div class="tweet-body">
    <div><span class="tweet-name">Halvorn</span> @ Halvorn</div>
    <div>Lorem Ipsum is simply dummy <span class="at">@ dummy text</span> of the printing and typesetting industry. Lorem Ipsum has been the industry's standard dummy text. Lorem Ipsum has been the industry's standard dummy text.</div>
    <div class="expand">Expand</div>
  </div>
</article>

<!-- footer -->
<footer class="footer abs">
  <nav class="footer-nav">
    <a href="#" style="left:269px">About Us</a>
    <a href="#" style="left:375px">Services</a>
    <a href="#" style="left:474px">Careers</a>
    <a href="#" style="left:579px">Contracts</a>
    <a href="#" style="left:682px">Contact</a>
  </nav>
  <p class="copyright"><b>© V9 GROUP</b> - 2014. All Rights Reserved.</p>
  <div class="social" style="left:683px">
    <svg width="50" height="51" viewBox="0 0 50 51" aria-hidden="true"><polygon points="25,1 49,13.5 49,37.5 25,50 1,37.5 1,13.5" fill="none" stroke="#fff" stroke-width="1.5"/></svg><span>Pals</span>
  </div>
  <div class="social" style="left:749px">
    <svg width="50" height="51" viewBox="0 0 50 51" aria-hidden="true"><polygon points="25,1 49,13.5 49,37.5 25,50 1,37.5 1,13.5" fill="none" stroke="#fff" stroke-width="1.5"/></svg><span>Chirp</span>
  </div>
  <div class="social" style="left:814px">
    <svg width="50" height="51" viewBox="0 0 50 51" aria-hidden="true"><polygon points="25,1 49,13.5 49,37.5 25,50 1,37.5 1,13.5" fill="none" stroke="#fff" stroke-width="1.5"/></svg><span>Nexa</span>
  </div>
</footer>

</body>
</html>
```